依頼詳細
ターゲットは20~40代の女性で『体験レッスンが無料』です。
体験レッスンの人数を増やしたいので、体験レッスンに行きたくなるようなバナーの制作をお願いいたします。
記載項目
・駅から徒歩1分
・手ぶらでOK
・無料体験レッスン実施中
サイズ
• 1200×1500と1080×1920の二種類
希望イメージ
シンプル 複雑
単色 カラフル
暗い 明るい
日常 高級
遊び心 厳粛
未来的 伝統的
女性的 男性的
希望する色
緑系
納品ファイル
• 高解像度JPG (.jpg)
• イラストレーター形式 (.ai)
補足説明
HPのURLは添付ファイルを参照ください。
■ 選んだ理由

今回の選んだ作品の気に入ったポイントは
「ルミナポストの広告バナー」として使用するという点で、一瞬流れた広告でも目が引くようなデザインと
こちらのヨガスタジオのコンセプトに合わせたハワイらしい明るくかわいらしいデザインがとても惹かれ、選出させていただきました。

■ 提案者全員のお礼・コメント

今回、たくさんの素敵なデザインのご提案
誠にありがとうございました。
どれも素敵な作品で、1つに絞るのがとても大変でした。
また、ご縁がありましたらどうぞ宜しくお願い申し上げます。
改めまして、今回ご提案してくださった皆様に心から感謝申し上げます。

```html
<!DOCTYPE html>
<html lang="ja">
<head>
<meta charset="UTF-8">
<title>ヨガスタジオ「Nalani」無料体験レッスン</title>
<link rel="stylesheet" href="https://fonts.googleapis.com/css2?family=Noto+Sans+JP:wght@400;500;700&display=swap">
<style>
  :root {
    --sky-top: #8fa6d6;
    --sky-mid: #c7a6d9;
    --sky-low: #f2b3cf;
    --palm: #1d2030;
    --panel: rgba(255, 255, 255, 0.82);
    --ink: #2f2a2a;
    --brown: #9e5430;
    --white: #ffffff;
    --sunset-a: #3a3036;
    --sunset-b: #b88a73;
    --spa-a: #d9d6d1;
    --spa-b: #f4f1ee;
    --band-blue: #a9cbe0;
    --band-pink: #f3a8c6;
    --band-peach: #f6c49a;
    --band-hot: #f08ab7;
  }
  * { margin: 0; padding: 0; box-sizing: border-box; }
  html, body { width: 675px; height: 1200px; overflow: hidden; }
  body { font-family: "Noto Sans JP", sans-serif; color: var(--ink); }
  .banner { position: relative; width: 675px; height: 1200px; overflow: hidden; }
  .backdrop {
    position: absolute; inset: 0;
    background:
      radial-gradient(ellipse at 15% 30%, rgba(29,32,48,0.55), transparent 45%),
      radial-gradient(ellipse at 90% 50%, rgba(29,32,48,0.5), transparent 40%),
      linear-gradient(180deg, var(--sky-top) 0%, var(--sky-mid) 45%, var(--sky-low) 100%);
  }
  .panel {
    position: absolute; left: 68px; top: 108px; width: 540px; height: 860px;
    background: linear-gradient(180deg, var(--panel) 0%, rgba(255,255,255,0.88) 70%, rgba(255,255,255,0.55) 100%);
  }
  .studio-name {
    position: absolute; top: 150px; width: 100%; text-align: center;
    font-size: 29px; font-weight: 500; letter-spacing: 1px;
  }
  .studio-mark {
    position: absolute; top: 248px; width: 100%; text-align: center;
    font-size: 22px; font-weight: 400; color: var(--brown);
  }
  .offer {
    position: absolute; left: 90px; top: 329px; width: 506px; height: 155px;
    background: var(--brown); color: var(--white); text-align: center;
  }
  .offer-lead { margin-top: 18px; font-size: 32px; font-weight: 500; letter-spacing: 1px; }
  .offer-price { margin-top: 12px; font-size: 30px; font-weight: 500; }
  .offer-price .zero { font-size: 58px; font-weight: 700; margin: 0 10px; vertical-align: -4px; }
  .photo { position: absolute; }
  .photo-yoga {
    left: 288px; top: 531px; width: 304px; height: 203px;
    background: linear-gradient(180deg, var(--sunset-a) 0%, var(--sunset-b) 55%, var(--sunset-a) 100%);
  }
  .photo-spa {
    left: 90px; top: 716px; width: 293px; height: 202px;
    background: linear-gradient(135deg, var(--spa-a) 0%, var(--spa-b) 60%, #f3c8d6 100%);
  }
  .band {
    position: absolute; height: 83px; display: flex; align-items: center;
    font-size: 33px; font-weight: 500;
  }
  .band-station {
    left: 236px; top: 945px; width: 439px; padding-left: 50px;
    background: linear-gradient(90deg, var(--band-blue) 0%, var(--band-pink) 60%, var(--band-peach) 100%);
    color: var(--ink);
  }
  .band-handsfree {
    left: 0; top: 1042px; width: 439px; padding-left: 55px;
    background: linear-gradient(90deg, var(--band-hot) 0%, var(--band-pink) 45%, var(--band-peach) 100%);
    color: var(--white);
  }
</style>
</head>
<body>
  <main class="banner">
    <div class="backdrop" role="img" aria-label="夕暮れの紫とピンクの空に広がるヤシの木のシルエット"></div>
    <div class="panel"></div>
    <h1 class="studio-name">ヨガスタジオ「Nalani」</h1>
    <p class="studio-mark">Nalani</p>
    <section class="offer">
      <p class="offer-lead">無料体験レッスン実施中</p>
      <p class="offer-price">今だけ<span class="zero">0</span>円</p>
    </section>
    <div class="photo photo-yoga" role="img" aria-label="夕日の海辺でヨガのポーズをとる女性のシルエット"></div>
    <div class="photo photo-spa" role="img" aria-label="タオルとボトル、ピンクのチューリップとキャンドルのスパ小物"></div>
    <p class="band band-station">駅から徒歩1分</p>
    <p class="band band-handsfree">手ぶらでOK</p>
  </main>
</body>
</html>
```